PowerPoint Listing Presentation for Real Estate Agency

We need a PowerPoint presentation for a new real estate brokerage team.

[[[[[[submit 1-3 sample slides for review - i will provide feedback and you can make changes if you want to - we will not be deciding on a design prior to the deadline]]]]]

******ATTN: DESIGNERS, if your skills are webdesign then just look at this like a portable website or a brochure. it should be easy enough******

NOTE: we have all the data to put into the slides. You just need to come up with the design and layout. we have a sample design that we like and have provided.

This focus will be for the home listing side of the business (a presentation for home sellers to convince them to use our services). The data and slides will present our team and the benefits, in the best light, to use our services over that of other real estate agent applying for the job. This presentation will proved facts and benefits and describe our special and unique offerings that will show a home seller why we can sell their home for more money in less time and with the least amount of hassle. The main color scheme is Dark Blue and White (we want some additional colors included - based on your creativity. otherwise the presentation will too monotone). We would like to see the use of Statistical Graphs (3-D) - data provided. We have photos of our team and a new logo (the logo could have some minor adjustment to clean it up if necessary) - also uploaded. We have about 80-90% of the information that will be put into the slides and will need to work closely to get the design and data integrated into the presentation (should be easier then it sounds). We should be able to add slides and data 'at will' over time via our master slides built into the presentation. We have a pretty good sample presentation that we like and can be used as a guideline (this is from our affiliated business network and we have full rights to all the information), it is uploaded but doesn't contain all the slide because of size limitations.

NOTE: An additional buyers presentation will be needed after we get the sellers presentation completed, which means additional work.

This should be enough to get you started and we are available if you have any questions to help you with the project. there will be around 60-70 total slides. once concept is completed it will be easy to create the slides.

Target Market(s)

home sellers. people who are moving to a new and better home or relocation for job reasons. typically more established in life

Industry/Entity Type

Real Estate

Requirements
Must have
• all the slides must be congruent. in other words, the exact same layout feel should used across the board. we are working on building our trade dress/image. Also, it must have a soft and inviting overall feel, yet show strength of ability.
Nice to have
• nice to have use of real people images when necessary. 3D graphs would be nice. clean modern look and feel, yet sophisticated and professional.
Should not have
• should not have a lot of time consuming transitions. do not include 3D stick figures or distracting moving gifs

```html
<!DOCTYPE html>
<html lang="en">
<head>
<meta charset="utf-8">
<title>Harwell &amp; Stone Team – Superior Results</title>
<link rel="stylesheet" href="https://fonts.googleapis.com/css2?family=Gelasio:wght@400&family=Play:wght@400&display=swap">
<style>
  :root {
    --navy: #0f2a5c;
    --sky: #5b8fd6;
    --gold: #f2b51d;
    --ink: #13285a;
    --accent-blue: #2c5fab;
    --white: #ffffff;
  }
  * { margin: 0; padding: 0; box-sizing: border-box; }
  html, body {
    width: 1200px; height: 900px; overflow: hidden;
    background: var(--white);
  }
  .slide {
    position: relative;
    width: 1200px; height: 900px;
    overflow: hidden;
    background: linear-gradient(180deg, #ffffff 0%, #eef3fa 55%, #dfe9f5 100%);
    font-family: "Gelasio", Georgia, serif;
  }
  .slide-frame { position: absolute; inset: 0; }
  .house-backdrop {
    position: absolute;
    left: 30px; top: 200px;
    width: 1040px; height: 560px;
    background: radial-gradient(ellipse at 45% 55%, rgba(160,185,215,0.28) 0%, rgba(190,210,232,0.14) 55%, rgba(255,255,255,0) 80%);
  }
  .footer-houses {
    position: absolute;
    left: 988px; top: 772px;
    width: 192px; height: 94px;
    border-radius: 6px;
    background: linear-gradient(180deg, rgba(255,255,255,0.30) 0%, rgba(255,255,255,0.16) 100%);
  }
  .brand-name {
    position: absolute;
    left: 24px; top: 24px;
    display: flex; align-items: center; gap: 10px;
    color: var(--white);
    font-size: 19px;
    line-height: 1.15;
    width: 170px;
  }
  .brand-square {
    width: 16px; height: 16px; flex: none;
    background: var(--white);
  }
  .slide-title {
    position: absolute;
    right: 102px; top: 22px;
    font-weight: 400;
    font-size: 41px;
    color: var(--ink);
    letter-spacing: 0.2px;
  }
  .slide-title .highlight { color: var(--accent-blue); }
  .benefit-list {
    position: absolute;
    left: 70px; top: 301px;
    list-style: none;
  }
  .benefit-item {
    display: flex; align-items: center;
    height: 94px;
    font-size: 35px;
    color: var(--ink);
    white-space: nowrap;
  }
  .benefit-item svg { width: 48px; height: 48px; margin-right: 26px; flex: none; }
  .team-footer {
    position: absolute;
    left: 80px; top: 836px;
    font-family: "Play", Arial, sans-serif;
    font-size: 36px;
    color: var(--white);
    letter-spacing: 0.5px;
  }
</style>
</head>
<body>
<main class="slide">
  <svg class="slide-frame" width="1200" height="900" viewBox="0 0 1200 900" aria-hidden="true">
    <defs>
      <linearGradient id="footerShade" x1="0" y1="0" x2="0" y2="1">
        <stop offset="0" stop-color="#4a4a4d"/>
        <stop offset="0.5" stop-color="#242426"/>
        <stop offset="1" stop-color="#111113"/>
      </linearGradient>
      <linearGradient id="headerShade" x1="0" y1="0" x2="0" y2="1">
        <stop offset="0" stop-color="#ffffff"/>
        <stop offset="1" stop-color="#eef3fa"/>
      </linearGradient>
      <linearGradient id="tickFill" x1="0" y1="0" x2="0" y2="1">
        <stop offset="0" stop-color="#fbd27a"/>
        <stop offset="1" stop-color="#ee9a2b"/>
      </linearGradient>
    </defs>

    <rect x="0" y="0" width="1200" height="100" fill="url(#headerShade)"/>
    <rect x="0" y="100" width="1200" height="3" fill="#9dbde3"/>

    <path d="M0 0 H430 C300 40 150 150 0 330 Z" fill="#9dc0ea"/>
    <path d="M0 0 H418 C290 40 140 150 0 312 Z" fill="var(--gold)"/>
    <path d="M0 0 H408 C282 38 132 146 0 300 Z" fill="var(--sky)"/>
    <path d="M0 0 H396 C272 36 124 140 0 286 Z" fill="var(--navy)"/>

    <path d="M1200 455 C1110 640 980 760 820 830 L1200 830 Z" fill="var(--sky)"/>
    <path d="M1200 468 C1112 650 985 768 830 838 L1200 838 Z" fill="var(--gold)"/>
    <path d="M1200 482 C1116 660 992 776 845 845 L1200 845 Z" fill="var(--navy)"/>

    <rect x="0" y="822" width="1200" height="78" fill="url(#footerShade)"/>
    <path d="M845 845 C900 822 930 810 960 790 L1200 790 L1200 900 L800 900 Z" fill="var(--navy)"/>
    <path d="M780 900 C830 880 880 855 845 845 L820 900 Z" fill="var(--navy)"/>

    <circle cx="1146" cy="50" r="31" fill="var(--white)"/>
    <circle cx="1146" cy="50" r="27" fill="var(--navy)"/>
    <g fill="none" stroke="#ffffff" stroke-width="3" stroke-linejoin="round">
      <path d="M1131 52 L1146 37 L1161 52"/>
      <path d="M1135 49 V64 H1157 V49"/>
    </g>
    <rect x="1149" y="53" width="5" height="5" fill="#ffffff"/>
  </svg>

  <div class="house-backdrop" role="img" aria-label="Faint illustration of a row of house outlines in pale blue"></div>
  <div class="footer-houses" role="img" aria-label="White outline illustration of three small houses"></div>

  <div class="brand-name"><span class="brand-square"></span><span>Harwell &amp; Stone</span></div>

  <h1 class="slide-title">You’ll Receive <span class="highlight">Superior Results</span></h1>

  <ul class="benefit-list">
    <li class="benefit-item">
      <svg viewBox="0 0 48 48" aria-hidden="true"><rect x="3" y="3" width="42" height="42" rx="10" fill="url(#tickFill)"/><rect x="12" y="14" width="22" height="22" fill="#ffffff" stroke="#2c5fab" stroke-width="2"/><path d="M14 24 L21 32 L38 9" fill="none" stroke="#1d4fa8" stroke-width="5" stroke-linecap="round" stroke-linejoin="round"/></svg>
      Our Unique Team System
    </li>
    <li class="benefit-item">
      <svg viewBox="0 0 48 48" aria-hidden="true"><rect x="3" y="3" width="42" height="42" rx="10" fill="url(#tickFill)"/><rect x="12" y="14" width="22" height="22" fill="#ffffff" stroke="#2c5fab" stroke-width="2"/><path d="M14 24 L21 32 L38 9" fill="none" stroke="#1d4fa8" stroke-width="5" stroke-linecap="round" stroke-linejoin="round"/></svg>
      Our Exclusive and Innovative Consumer Programs
    </li>
    <li class="benefit-item">
      <svg viewBox="0 0 48 48" aria-hidden="true"><rect x="3" y="3" width="42" height="42" rx="10" fill="url(#tickFill)"/><rect x="12" y="14" width="22" height="22" fill="#ffffff" stroke="#2c5fab" stroke-width="2"/><path d="M14 24 L21 32 L38 9" fill="none" stroke="#1d4fa8" stroke-width="5" stroke-linecap="round" stroke-linejoin="round"/></svg>
      Our Leading Edge Technology
    </li>
    <li class="benefit-item">
      <svg viewBox="0 0 48 48" aria-hidden="true"><rect x="3" y="3" width="42" height="42" rx="10" fill="url(#tickFill)"/><rect x="12" y="14" width="22" height="22" fill="#ffffff" stroke="#2c5fab" stroke-width="2"/><path d="M14 24 L21 32 L38 9" fill="none" stroke="#1d4fa8" stroke-width="5" stroke-linecap="round" stroke-linejoin="round"/></svg>
      Our Specialized Skill
    </li>
  </ul>

  <p class="team-footer">The Harwell &amp; Stone Team</p>
</main>
</body>
</html>
```